SKYVANTEX (drone photo and video) and Photogrammetry Services (mapping and 3D modeling)

We need a business card design for a SKYVANTEX. Our businesses provides (drone) Aerial Photo and Video Captures. However we also provide Photogrammetry (which is 3D modeling and mapping). We greatly value unique points of view taken of landscapes and subjects with aerial photography and videography. 3D modeling and mapping is the other area of focus and have an incredibly broad scope of applications and imaginative creativity.

Target Market(s)

Based out of Northern Virginia and serving the greater Virginia and Maryland areas

Industry/Entity Type

Drone Photo and video and Photogrammetry Services (mapping and 3D modeling)

Contact Information for Business Card

3D Models, Maps and Photo/Video Production name: Marcus Pettibone email: mqp@skyvantex.us website: skyvantex.us phone: 571-806-3394; please also include "Aerial Photo/Video and 3D Mapping/Modeling"

Requirements
Must have
• Please make this design vertical and double sided. The selection box is not letting me choose Double Sided but that is my wish. Incorporate uploaded LOGO and color scheme
Nice to have
• Preferably does not feel too crowded and balances not having an exaggerated amount of distracting detail
Should not have
• do not cram bullet points or text in long form

```html
<!DOCTYPE html>
<html lang="en">
<head>
<meta charset="utf-8">
<title>SKYVANTEX business card</title>
<link rel="stylesheet" href="https://fonts.googleapis.com/css2?family=Marcellus&display=swap">
<style>
  :root {
    --backdrop: #5f6062;
    --paper: #f4f4f4;
    --ink: #070707;
    --text: #1b1b1b;
    --muted: #555555;
    --red: #e31e2d;
    --yellow: #f2b21c;
    --orange: #ef7d23;
    --card-w: 380px;
    --card-h: 665px;
  }
  * { box-sizing: border-box; margin: 0; padding: 0; }
  html, body { width: 1200px; height: 900px; overflow: hidden; }
  body {
    background: var(--backdrop);
    font-family: "Marcellus", serif;
    display: flex;
    align-items: center;
    justify-content: center;
    gap: 100px;
  }
  .card {
    position: relative;
    width: var(--card-w);
    height: var(--card-h);
    overflow: hidden;
    box-shadow: 0 12px 28px rgba(0,0,0,0.35);
  }
  .card--front { background: var(--paper); }
  .card--back { background: var(--ink); }
  .card__shapes {
    position: absolute;
    inset: 0;
    width: 100%;
    height: 100%;
  }
  .brand {
    position: absolute;
    left: 0;
    right: 0;
    display: flex;
    align-items: center;
    justify-content: center;
    gap: 12px;
  }
  .card--front .brand { top: 110px; }
  .card--back .brand { top: 270px; }
  .brand__dot {
    width: 30px;
    height: 30px;
    border-radius: 50%;
    background: var(--orange);
    flex: none;
  }
  .brand__name {
    font-size: 40px;
    letter-spacing: 2px;
    line-height: 1;
  }
  .card--front .brand__name { color: var(--ink); }
  .card--back .brand__name { color: #ffffff; }
  .details {
    position: absolute;
    left: 52px;
    right: 30px;
    top: 292px;
  }
  .details__name {
    font-size: 24px;
    line-height: 1.2;
    color: var(--ink);
  }
  .details__role {
    margin-top: 4px;
    font-size: 13.5px;
    line-height: 1.3;
    color: var(--red);
  }
  .contact {
    margin-top: 22px;
    list-style: none;
    display: flex;
    flex-direction: column;
    gap: 11px;
  }
  .contact__item {
    display: flex;
    align-items: center;
    gap: 12px;
    font-size: 19px;
    line-height: 1.2;
    color: var(--text);
  }
  .contact__icon { width: 20px; height: 20px; flex: none; }
</style>
</head>
<body>

<section class="card card--front" aria-label="Card front">
  <svg class="card__shapes" viewBox="0 0 380 665" aria-hidden="true">
    <polygon points="380,462 380,505 195,566 180,561" fill="var(--yellow)"/>
    <polygon points="380,505 380,648 195,566" fill="var(--red)"/>
    <polygon points="0,478 380,648 380,665 0,665" fill="var(--ink)"/>
  </svg>
  <div class="brand">
    <span class="brand__dot"></span>
    <span class="brand__name">SKYVANTEX</span>
  </div>
  <div class="details">
    <p class="details__name">Marcus Pettibone</p>
    <p class="details__role">Aerial Photo/Video and 3D Mapping/Modeling</p>
    <ul class="contact">
      <li class="contact__item">
        <svg class="contact__icon" viewBox="0 0 24 24" aria-hidden="true">
          <path d="M6 3h3l2 5-2 1.5a11 11 0 0 0 5.5 5.5L16 13l5 2v3a3 3 0 0 1-3 3A16 16 0 0 1 3 6a3 3 0 0 1 3-3z" fill="var(--red)"/>
        </svg>
        <span>571-806-3394</span>
      </li>
      <li class="contact__item">
        <svg class="contact__icon" viewBox="0 0 24 24" aria-hidden="true">
          <rect x="2" y="5" width="20" height="14" rx="2" fill="var(--red)"/>
          <path d="M3 6l9 7 9-7" fill="none" stroke="#fff" stroke-width="1.6"/>
        </svg>
        <span>mqp@skyvantex.us</span>
      </li>
      <li class="contact__item">
        <svg class="contact__icon" viewBox="0 0 24 24" aria-hidden="true">
          <circle cx="12" cy="12" r="9" fill="none" stroke="var(--red)" stroke-width="2"/>
          <path d="M3 12h18M12 3c3 3 3 15 0 18M12 3c-3 3-3 15 0 18" fill="none" stroke="var(--red)" stroke-width="1.4"/>
        </svg>
        <span>www.skyvantex.us</span>
      </li>
    </ul>
  </div>
</section>

<section class="card card--back" aria-label="Card back">
  <svg class="card__shapes" viewBox="0 0 380 665" aria-hidden="true">
    <polygon points="0,540 272,570 262,584 0,566" fill="var(--yellow)"/>
    <polygon points="0,566 262,584 170,665 0,665" fill="var(--red)"/>
    <polygon points="380,420 380,665 170,665 262,584 272,570" fill="var(--paper)"/>
  </svg>
  <div class="brand">
    <span class="brand__dot"></span>
    <span class="brand__name">SKYVANTEX</span>
  </div>
</section>

</body>
</html>
```